Modern and appealing business Wordpress site

I've been operating my consulting firm for 5 years and feel like it is time to really improve on my web presence as I'm starting to get more national attention. I had a logo made through this service a couple of years ago, and would like to get a website that matches the look of it. The website will be used to (1) advertise my services (2) provide a brief overview of our management philosophies, and (3) host a resource library database. I understand HTML, but am not as familiar with how to code Wordpress, so I need someone that can help upload themes.

The website can be found at www.trbvexlane.com.

For design, I prefer round designs to square and want the color scheme to match the attached logo. I have included both the full logo and the abbreviated one.

I also have a new picture for CFO uploaded. I plan on getting a new one for the CEO in the coming weeks, so I would like someone that I could get to help make the modification at a later time.

The resource database will be put into a document library (probably Plix4) once the final design is completed rather than having multiple pages with links...just so you know the final vision for the site.

Reach out if you have any questions.

Target Market(s)

Community Action Agencies, Nonprofit Organization Leaders

Industry/Entity Type

Consulting

Coding

Coded - Design and coding required

Font styles to use
Sans Serif

Requirements
Must have
• Must match the color scheme of the attached logo

```html
<!DOCTYPE html>
<html lang="en">
<head>
<meta charset="utf-8">
<title>Services – TRB Vexlane</title>
<link href="https://fonts.googleapis.com/css2?family=Montserrat:wght@500;600;700;800&family=Open+Sans:wght@400;600&display=swap" rel="stylesheet">
<style>
:root{
  --blue:#2a9fd8;
  --blue-dark:#1c7fb4;
  --ink:#2b2b2b;
  --text:#3d3d3d;
  --footer:#2a2a2a;
  --topbar:#2f2f2f;
  --white:#ffffff;
  --muted:#9a9a9a;
}
*{margin:0;padding:0;box-sizing:border-box}
html,body{width:1200px;height:3132px;overflow:hidden}
body{position:relative;background:var(--white);font-family:"Open Sans",sans-serif;color:var(--text)}
.topbar{position:absolute;left:0;top:0;width:1200px;height:40px;background:var(--topbar);color:var(--white);font-size:14px;display:flex;align-items:center;padding:0 88px}
.topbar .pin{display:flex;align-items:center;gap:8px}
.topbar .phone{position:absolute;left:600px;display:flex;align-items:center;gap:8px}
.social{display:flex;gap:8px}
.topbar .social{position:absolute;right:88px}
.social span{width:26px;height:26px;border-radius:50%;background:var(--blue);display:block}
.nav{position:absolute;top:40px;left:0;width:1200px;height:112px;display:flex;align-items:center;padding:0 88px}
.brand{display:flex;align-items:center;gap:10px;font-family:"Montserrat",sans-serif;font-weight:800;font-size:30px;color:var(--ink);letter-spacing:1px}
.brand i{width:34px;height:34px;border-radius:50%;background:var(--blue);display:block}
.menu{margin-left:auto;display:flex;align-items:center;gap:34px;font-family:"Montserrat",sans-serif;font-size:15px;font-weight:600;color:var(--ink);text-transform:uppercase}
.menu .active{color:var(--blue)}
.menu .cta{background:var(--blue);color:var(--white);padding:14px 30px;border-radius:30px}
.hero{position:absolute;top:152px;left:0;width:1200px;height:330px;background:linear-gradient(100deg,#3d4a5a 0%,#6b7683 35%,#8a8f95 60%,#4b5563 100%);overflow:hidden}
.hero h1{position:absolute;top:120px;width:100%;text-align:center;font-family:"Montserrat",sans-serif;font-size:56px;font-weight:800;color:var(--white);letter-spacing:2px}
.wave{position:absolute;bottom:0;left:0;display:block}
.intro{position:absolute;top:540px;left:92px;width:1016px;font-size:16px;line-height:1.75}
.intro p{margin-bottom:28px}
.photo{position:absolute;width:384px;height:384px;border-radius:50%;border:12px solid var(--blue);border-top-color:transparent;border-right-color:transparent;transform:rotate(-20deg)}
.photo div{width:100%;height:100%;border-radius:50%;transform:rotate(20deg)}
.block{position:absolute}
.block h2{font-family:"Montserrat",sans-serif;font-size:24px;font-weight:800;color:var(--ink);margin-bottom:20px;letter-spacing:.5px}
.ticks{list-style:none;font-size:16px;line-height:1.9}
.ticks li{position:relative;padding-left:32px}
.ticks li::before{content:"";position:absolute;left:0;top:8px;width:18px;height:18px;border-radius:50%;background:var(--blue)}
.ticks li::after{content:"";position:absolute;left:6px;top:11px;width:5px;height:9px;border:solid var(--white);border-width:0 2px 2px 0;transform:rotate(45deg)}
.footer{position:absolute;left:0;top:2720px;width:1200px;height:412px}
.footer .wave{top:0;bottom:auto}
.footer .body{position:absolute;top:60px;left:0;width:1200px;height:352px;background:var(--footer);color:var(--white);padding:50px 92px 0;display:flex}
.footer .brand{color:var(--white)}
.fcol{font-size:15px;line-height:1.75}
.fcol h3{font-family:"Montserrat",sans-serif;font-size:17px;font-weight:700;margin-bottom:12px;padding-left:14px;border-left:4px solid var(--blue)}
.fcol ul{list-style:none;padding-left:18px}
.copy{margin-top:20px;font-size:13px;color:var(--muted);line-height:1.6}
.contact-row{display:flex;align-items:flex-start;gap:14px;margin-bottom:22px;padding-left:18px}
.contact-row i{width:40px;height:40px;border-radius:50%;background:var(--blue);display:flex;align-items:center;justify-content:center;flex:none}
</style>
</head>
<body>
<header class="topbar">
  <div class="pin"><svg width="12" height="16" viewBox="0 0 12 16"><path d="M6 0a6 6 0 0 0-6 6c0 4.5 6 10 6 10s6-5.5 6-10a6 6 0 0 0-6-6zm0 8.5A2.5 2.5 0 1 1 6 3.5a2.5 2.5 0 0 1 0 5z" fill="#fff"/></svg><span><b>Address :</b> 418 Marlow Ridge, Alder Falls, Georgia 30417</span></div>
  <div class="phone"><svg width="14" height="14" viewBox="0 0 24 24"><path d="M6.6 10.8a15 15 0 0 0 6.6 6.6l2.2-2.2a1 1 0 0 1 1-.25 11.4 11.4 0 0 0 3.6.6 1 1 0 0 1 1 1V20a1 1 0 0 1-1 1A17 17 0 0 1 3 4a1 1 0 0 1 1-1h3.5a1 1 0 0 1 1 1c0 1.25.2 2.45.6 3.6a1 1 0 0 1-.25 1z" fill="#fff"/></svg><span>Call Us : (706) 555-0148</span></div>
  <div class="social"><span></span><span></span><span></span><span></span></div>
</header>

<nav class="nav">
  <div class="brand"><i></i>VEXLANE</div>
  <div class="menu">
    <span class="active">Services</span><span>Calendar</span><span>RAMP</span><span>MAVEN</span><span>Our Team</span><span>Resources</span><span class="cta">Contact</span>
  </div>
</nav>

<section class="hero" role="img" aria-label="Photo of business people meeting around a laptop">
  <h1>SERVICES</h1>
  <svg class="wave" width="1200" height="90" viewBox="0 0 1200 90" preserveAspectRatio="none">
    <path d="M0 40 Q600 110 1200 20 L1200 90 L0 90Z" fill="#2a9fd8"/>
    <path d="M0 62 Q600 120 1200 40 L1200 90 L0 90Z" fill="#fff"/>
  </svg>
</section>

<section class="intro">
  <p>We understand that you have many options when shopping for a consulting firm, so why chose us?</p>
  <p>Although we are a for-profit corporation, our business philosophy is based on the same Mission Focused Data Informed (MFDI) mentality that we teach our customers. Our goal is not simply to generate revenue, but to empower each organization to fulfill their purpose in innovative ways.</p>
  <p>Our team of staff, contractors, and advisors include real people who have been where you are and have identified practical solutions to the problems you face every day. We are dedicated to your success and look forward to working with you.</p>
</section>

<div class="photo" style="left:88px;top:880px"><div role="img" aria-label="Photo of two consultants reviewing papers at a table" style="background:linear-gradient(135deg,#b9a58c,#6e5d4d 60%,#3b3a3c)"></div></div>
<section class="block" style="left:536px;top:948px">
  <h2>CONSULTING</h2>
  <ul class="ticks">
    <li>General Operations Consulting</li>
    <li>RAMP Implementation Consulting</li>
    <li>Leadership Transition Assistance</li>
    <li>SWOT Analysis Development</li>
    <li>Strategic/Action Plan Development</li>
    <li>Corrective Action Plan Development</li>
  </ul>
</section>

<section class="block" style="left:92px;top:1330px">
  <h2>TRAINING (TRENDING TOPICS)</h2>
  <ul class="ticks">
    <li>Introduction to RAMP</li>
    <li>Practical Application RAMP</li>
    <li>The Mission Focused Data Informed Mentality</li>
    <li>Understanding the Purpose of Community Action</li>
    <li>Assessing Community</li>
    <li>Developing Plans that are Strategic</li>
    <li>Collective Impact Strategies</li>
    <li>Board Duties and Responsibilities</li>
    <li>Case Management</li>
    <li>Using Trackwell to Measure Organizational Success</li>
  </ul>
</section>
<div class="photo" style="left:720px;top:1360px"><div role="img" aria-label="Photo of a trainer presenting at a whiteboard to a group" style="background:linear-gradient(135deg,#e6e8ea,#9aa3ab 55%,#2f3338)"></div></div>

<div class="photo" style="left:88px;top:1820px"><div role="img" aria-label="Photo of hands reviewing charts on a laptop and printouts" style="background:linear-gradient(135deg,#d9dde2,#8fa9bf 55%,#45525f)"></div></div>
<section class="block" style="left:536px;top:1878px">
  <h2>DATA &amp; ANALYTICS</h2>
  <ul class="ticks">
    <li>Community Assessment Development</li>
    <li>Data Quality Assurance Evaluations</li>
    <li>Organizational Impact Analysis</li>
    <li>Program Performance Analysis</li>
  </ul>
</section>

<section class="block" style="left:92px;top:2396px">
  <h2>STORYTELLING</h2>
  <ul class="ticks">
    <li>Report Development</li>
    <li>Videography</li>
  </ul>
</section>
<div class="photo" style="left:720px;top:2262px"><div role="img" aria-label="Photo of a video camera recording an interview" style="background:linear-gradient(135deg,#cfd4cf,#6f7a72 55%,#222)"></div></div>

<footer class="footer">
  <svg class="wave" width="1200" height="90" viewBox="0 0 1200 90" preserveAspectRatio="none">
    <path d="M0 20 Q600 100 1200 10 L1200 90 L0 90Z" fill="#2a9fd8"/>
    <path d="M0 45 Q600 115 1200 35 L1200 90 L0 90Z" fill="#2a2a2a"/>
  </svg>
  <div class="body">
    <div class="fcol" style="width:260px">
      <div class="brand"><i></i>VEXLANE</div>
      <div class="social" style="margin-top:22px"><span></span><span></span><span></span><span></span></div>
      <p class="copy">Copyright © 2022 TRB Vexlane.<br>All rights reserved</p>
    </div>
    <div class="fcol" style="width:240px;margin-left:20px">
      <h3>QUICK LINKS</h3>
      <ul><li>Services</li><li>Calendar</li><li>RAMP</li><li>MAVEN</li><li>Our Team</li><li>Contact</li></ul>
    </div>
    <div class="fcol" style="width:260px">
      <h3>OTHER LINKS</h3>
      <ul><li>RAMP Resources</li><li>RAMP PTC</li><li>CAP Resources</li><li>NSCPA Resources</li><li>CAPLEX Resources</li><li>GoalPath Technology</li></ul>
    </div>
    <div class="fcol" style="width:280px">
      <h3>CONTACT INFO</h3>
      <div class="contact-row"><i><svg width="14" height="18" viewBox="0 0 12 16"><path d="M6 0a6 6 0 0 0-6 6c0 4.5 6 10 6 10s6-5.5 6-10a6 6 0 0 0-6-6zm0 8.5A2.5 2.5 0 1 1 6 3.5a2.5 2.5 0 0 1 0 5z" fill="#fff"/></svg></i><span>418 Marlow Ridge<br>Alder Falls, Georgia 30417</span></div>
      <div class="contact-row"><i><svg width="16" height="16" viewBox="0 0 24 24"><path d="M6.6 10.8a15 15 0 0 0 6.6 6.6l2.2-2.2a1 1 0 0 1 1-.25 11.4 11.4 0 0 0 3.6.6 1 1 0 0 1 1 1V20a1 1 0 0 1-1 1A17 17 0 0 1 3 4a1 1 0 0 1 1-1h3.5a1 1 0 0 1 1 1c0 1.25.2 2.45.6 3.6a1 1 0 0 1-.25 1z" fill="#fff"/></svg></i><span style="line-height:40px">(706) 555-0148</span></div>
    </div>
  </div>
</footer>
</body>
</html>
```